Brochure for a paper wholesaler who wants to educate his print industry clients

We will be making a stapled informative brochure, that contains basic information about our paper products - the types of paper there is, their characteristics and other useful information.
As we are part of a paper wholesaler group in Europe - ORVANTE, we received a brochure in German that has this kind of information. The text in it is not as important. What is important is the layout of the document and how the text will appear in it (added in the uploaded files - 210915_Wiessenswertes_TKLM_F51.pdf).
We are allowed to tinker with this file and adjust it to our needs. So there are also .idml and .indd files available (also in the uploaded files).
We would like to keep the custom page size of 210 x290mm (8.3x11.4 in), or you can go up to 210x297mm (8.3x11.7 in).
What we want is a modern looking design that contains our companies red bordo and white/ grey colours to replace the existing green colours in this borchure. The pictures and appearance of the file can be changed according to your views and what you think would look good. We don't necessarily want to keep the same design, we just want the layout of the document be the same, as we will be placing our translated text into it. The ORVANTE logo should be replaced with our own logo (KEMSU Logo.png).
As for how it could look, it could go together with our paper presentation, for which the design can be seen in the "KEMSU Base - v2.pptx".
Holiday season, so have a lot of tasks to take care of and not as much time to check PixelForge as often.

```html
<!DOCTYPE html>
<html lang="de">
<head>
<meta charset="utf-8">
<title>Wissenswert! – Broschüre Titelseite</title>
<link rel="stylesheet" href="https://fonts.googleapis.com/css2?family=Josefin+Sans:ital,wght@0,300;0,400;0,600;1,300&display=swap">
<style>
  :root {
    --stage: #a7a7a7;
    --blush: #f4c3c1;
    --rose: #d9a3a2;
    --dusty: #b66f72;
    --bordo: #8a3a40;
    --bordo-deep: #7a2a31;
    --paper: #ffffff;
    --ink-soft: rgba(255,255,255,0.9);
    --brand-ink: #8c4a4e;
  }
  * { box-sizing: border-box; margin: 0; padding: 0; }
  html, body {
    width: 1200px; height: 900px; overflow: hidden;
    background: var(--stage);
    font-family: "Josefin Sans", sans-serif;
  }
  .canvas {
    width: 1200px; height: 900px;
    display: flex; align-items: center; justify-content: center;
  }
  .cover {
    position: relative;
    width: 580px; height: 800px;
    overflow: hidden;
    box-shadow: 0 6px 18px rgba(0,0,0,0.18);
  }
  .cover-art {
    position: absolute; inset: 0;
    background:
      linear-gradient(135deg, rgba(255,255,255,0.25) 0%, rgba(255,255,255,0) 40%),
      linear-gradient(180deg, var(--blush) 0%, var(--rose) 35%, var(--dusty) 62%, var(--bordo) 85%, var(--bordo-deep) 100%);
  }
  .cover-band {
    position: absolute; left: 0; right: 0; bottom: 70px; height: 1px;
    background: rgba(255,255,255,0.18);
  }
  .brand {
    position: absolute; top: 110px; left: 0; right: 0;
    display: flex; align-items: center; justify-content: center; gap: 8px;
    padding-left: 60px;
  }
  .brand-dot {
    width: 9px; height: 9px; border-radius: 50%;
    background: var(--brand-ink);
  }
  .brand-name {
    font-weight: 600; font-size: 17px; letter-spacing: 0.04em;
    color: var(--brand-ink);
  }
  .title-block {
    position: absolute; left: 58px; top: 555px; right: 40px;
    color: var(--paper);
  }
  .series-label {
    display: inline-block;
    font-size: 9px; font-weight: 300; letter-spacing: 0.08em;
    text-transform: uppercase;
    padding-bottom: 3px;
    border-bottom: 2px solid var(--paper);
    margin-bottom: 8px;
  }
  .headline {
    font-weight: 400; font-size: 27px; line-height: 1.05;
    text-transform: uppercase; letter-spacing: 0.01em;
  }
  .subline {
    margin-top: 20px; padding-left: 22px;
    font-size: 10px; font-weight: 300; font-style: italic;
    letter-spacing: 0.05em; color: var(--ink-soft);
  }
</style>
</head>
<body>
<main class="canvas">
  <article class="cover">
    <div class="cover-art" role="img" aria-label="Abstrakte, sich kreuzende diagonale Lichtstreifen in Rosé- und Bordeauxtönen"></div>
    <div class="cover-band"></div>
    <header class="brand">
      <span class="brand-dot"></span>
      <span class="brand-name">KEMSU</span>
    </header>
    <section class="title-block">
      <span class="series-label">Paper &amp; Print</span>
      <h1 class="headline">Wissenswert!<br>Formate, Klassen,<br>Farben, Berechnungen</h1>
      <p class="subline">Wegweiser für den Umgang mit Papier und Karton</p>
    </section>
  </article>
</main>
</body>
</html>
```